Buchcover-Design für Fragenbuch
Ganz herzlichen Dank. Die Zusammenarbeit war völlig reibungslos und entspannt. Änderungswünsche wurden professionell umgesetzt und die kreativen Vorschläge fand ich super. Ich bin total glücklich mit dem Ergebnis.
Zielgruppe
Autorin und Workshopleiterin. Zielgruppe: Frauen ab 30
Aufgabenstellung
Ich benötige ein komplettes Buchcover, sowie 12 farbige Innenseiten. Es geht um ein Fragenbuch zum Ausfüllen mit dem Titel:
„Finde zurück zur leisen Mitte
Ein Arbeitsheft zum Eintragen für tiefere seelische Ruhe“
Das Format des Buches beträgt 17x22cm. Es ist in 12 Wochen unterteilt. Darum hätte ich gerne zwischen den einzelnen Wochen eine farbige Seite (1. Woche, 2. Woche etc.), die designmäßig mit dem Außencover korrespondiert.
Die Farben sollten eher zart oder gedeckt sein. Auf keinen Fall jedoch kitschig. Wichtig ist mir, dass keine bestimmte Person zu sehen ist. (Foto)
Das ist meine Website www.finde-zurueck-zur-leisen-mitte.de

```html
<!DOCTYPE html>
<html lang="de">
<head>
<meta charset="utf-8">
<title>Finde zurück zur leisen Mitte – Cover und Wochenseite</title>
<link rel="stylesheet" href="https://fonts.googleapis.com/css2?family=Crimson+Text:wght@400;600&family=Jost:wght@300;400&family=Great+Vibes&display=swap">
<style>
  :root {
    --canvas: #ffffff;
    --paper: #dcd0c5;
    --paper-right: #ddd1c5;
    --accent: #b89e86;
    --frame: #b39a7d;
    --ink: #2a1f1a;
    --sand-light: #e4e1dc;
    --sand-dark: #b9b4ad;
    --candle-light: #dcdcdc;
    --candle-dark: #8f8a86;
  }
  * { margin: 0; padding: 0; box-sizing: border-box; }
  html, body {
    width: 1200px; height: 849px; overflow: hidden;
    background: var(--canvas);
  }
  .stage { position: relative; width: 1200px; height: 849px; }

  .page {
    position: absolute; top: 184px; height: 468px;
    color: var(--ink); overflow: hidden;
  }
  .page--cover { left: 233px; width: 361px; background: var(--paper); }
  .page--week  { left: 662px; width: 364px; background: var(--paper-right); }

  .photo { position: absolute; left: 0; top: 0; width: 100%; }
  .photo--sand {
    height: 241px;
    background: linear-gradient(150deg, var(--sand-light) 0%, #cfcbc5 45%, var(--sand-dark) 100%);
  }
  .photo--candle {
    height: 161px;
    background: radial-gradient(circle at 48% 70%, #e9d9b8 0%, #a89a8a 14%, transparent 26%),
                linear-gradient(160deg, var(--candle-light) 0%, #c6c6c6 55%, var(--candle-dark) 100%);
  }

  .frame { position: absolute; pointer-events: none; }
  .frame--cover {
    left: 33px; right: 37px; top: 23px; bottom: 24px;
    border: 1px solid var(--frame);
  }
  .frame--week {
    left: 36px; right: 38px; top: 161px; bottom: 24px;
    border: 1px solid var(--frame); border-top: none;
  }

  .cover-title {
    position: absolute; top: 259px; left: 0; width: 100%;
    text-align: center;
    font-family: "Crimson Text", serif; font-weight: 400;
    font-size: 14.5px; letter-spacing: 0.2px; text-transform: uppercase;
  }
  .cover-subtitle {
    position: absolute; top: 309px; left: 0; width: 100%;
    text-align: center;
    font-family: "Jost", sans-serif; font-weight: 300;
    font-size: 18px; letter-spacing: 0.3px; text-transform: uppercase;
  }
  .cover-tagline {
    position: absolute; top: 339px; left: 0; width: 100%;
    text-align: center;
    font-family: "Jost", sans-serif; font-weight: 400;
    font-size: 7px; line-height: 11px; text-transform: uppercase;
  }
  .cover-author {
    position: absolute; top: 382px; left: 0; width: 100%;
    text-align: center;
    font-family: "Great Vibes", cursive; font-size: 17px;
  }
  .cover-band {
    position: absolute; left: 71px; top: 430px; width: 220px; height: 29px;
    background: var(--accent);
    display: flex; justify-content: space-around; align-items: center;
    font-family: "Crimson Text", serif; font-size: 7px; text-transform: uppercase;
  }

  .week-title {
    position: absolute; top: 250px; left: 0; width: 100%;
    text-align: center;
    font-family: "Crimson Text", serif; font-weight: 400;
    font-size: 17px; text-transform: uppercase;
  }
  .week-badge {
    position: absolute; left: 85px; top: 306px; width: 181px; height: 162px;
    background: var(--accent); text-align: center;
  }
  .week-number {
    position: absolute; left: 0; width: 100%; top: 20px;
    font-family: "Jost", sans-serif; font-weight: 300;
    font-size: 76px; line-height: 1;
  }
  .week-label {
    position: absolute; left: 10px; width: 100%; top: 102px;
    font-family: "Jost", sans-serif; font-weight: 300;
    font-size: 30px; line-height: 1;
  }
</style>
</head>
<body>
<main class="stage">
  <section class="page page--cover" aria-label="Buchcover">
    <div class="photo photo--sand" role="img" aria-label="Foto: hellgraue Sanddünen mit geschwungenen Windrippen"></div>
    <div class="frame frame--cover"></div>
    <h1 class="cover-title">Finde zurück zur leisen Mitte</h1>
    <p class="cover-subtitle">Ein Arbeitsheft</p>
    <p class="cover-tagline">zum Eintragen<br>für tiefere seelische Ruhe</p>
    <p class="cover-author">by Lena Morwald</p>
    <div class="cover-band">
      <span>Coaching</span><span>Mentoring</span><span>2021</span>
    </div>
  </section>

  <section class="page page--week" aria-label="Wochenseite">
    <div class="photo photo--candle" role="img" aria-label="Foto: brennende Kerze in einem braunen Glas auf hellem Tisch"></div>
    <div class="frame frame--week"></div>
    <h2 class="week-title">Title here</h2>
    <div class="week-badge">
      <span class="week-number">4</span>
      <span class="week-label">WOCHE</span>
    </div>
  </section>
</main>
</body>
</html>
```